Cold Pressed Juice Cleanse Brochure

We need to update our existing brochure (attached) with new photography. The wording can remain the same, however, on the CLEANSE ORDER page (panel 3), make these changes. You can also consult our website for additional design ideas. www.brightmarlowtonic.com.au

Upon waking, drink your first juice, and drink your next juice in order every two hours thereafter.

Harbour Cleanse. This is our most popular cleanse & perfect for those who want to balance great-tasting juices with high efficiency. This bundle includes:
1. Greens Smoothie
2. Ember Fizzwater or Spicy red
3. Green A
4. Red or Sweet Carrot
5. Green B
6. Either Silk Pour

Meadow Cleanse
Our most intense & lowest calorie cleanse - you get the maximum results in the minimum amount of time. This bundle includes:
1. Fern Kick or Celery
2. Ember Fizzwater
3. Green Smoothie
4. Green B
5. Green A
6. Oatbloom Drinkable

Hearth Cleanse
The organic Hearth Cleanse. We've curated a mixture of smoothies, cold-pressed juices, bone broth and nut mylks to keep you clean and warm through the winter months. The broth together with our Ember Fizzwater and Oatbloom Drinkable can all be gently heated on the stove to nourish you from the inside and out. This bundle includes:
1. Green Smoothie
2. Ember Fizzwater or Spicy Red
3. Sweet Carrot or Red
4. Organic Bone Broth
5. Green B
6. Either Silk Pour

We truly believe in our Cleanses and the results speak for themselves. NOURISH your body with antioxidant-rich juices. HELP your digestion and encourage a healthy balance of flora in your belly. ENJOY better overall well-being and weight loss.

Target Market(s)

25-60 year old M & F

Industry/Entity Type

Health And Wellness

Requirements
Must have
• The info on the existing brochure together with the new information listed in the project description.

```html
<!DOCTYPE html>
<html lang="en">
<head>
<meta charset="utf-8">
<title>Cleanse Tips Brochure</title>
<link href="https://fonts.googleapis.com/css2?family=Questrial&family=Montserrat:ital,wght@0,600;0,700;1,500;1,700&display=swap" rel="stylesheet">
<style>
  :root{
    --green:#3cb33e;
    --green-dark:#2e8f31;
    --ink:#1d1d1d;
    --text:#333;
    --paper:#ffffff;
    --backdrop:#e6e6e6;
    --leaf:#6fbf4a;
  }
  *{box-sizing:border-box;margin:0;padding:0}
  html,body{width:1200px;height:2400px;overflow:hidden}
  body{background:var(--backdrop);font-family:"Questrial",sans-serif;color:var(--text);position:relative}
  .spread{position:absolute;left:40px;width:1120px;height:792px;background:var(--paper);box-shadow:0 6px 24px rgba(0,0,0,.12);display:flex}
  .spread--outside{top:300px}
  .spread--inside{top:1300px}
  .panel{position:relative;width:373.33px;height:100%;border-right:1px solid #eee;overflow:hidden}
  .panel:last-child{border-right:none}
  .photo{position:absolute;border-radius:4px}
  .photo--table{background:radial-gradient(ellipse at 50% 50%,#9bd36a 0%,#5fae3c 30%,#e9efe6 62%,#f4f4f2 100%)}
  .photo--bottles{background:linear-gradient(90deg,#4caf3a 0%,#6cc04a 28%,#f0a12a 45%,#e2612a 58%,#8c1f3a 70%,#e8d7c4 86%,#f6efe6 100%)}
  .photo--greens{background:linear-gradient(90deg,#4caf3a,#68bd45 55%,#e9d9c6)}
  .brand{display:flex;align-items:center;gap:10px;font-family:"Montserrat",sans-serif;font-weight:600;color:var(--ink);font-size:26px;letter-spacing:-.3px}
  .brand__dot{width:34px;height:34px;border-radius:50%;background:var(--green);flex:none}
  .heading{font-family:"Questrial",sans-serif;font-size:30px;color:var(--ink);letter-spacing:.5px}
  .heading b{font-family:"Montserrat",sans-serif;font-weight:700;color:var(--green)}
  .heading i{font-family:"Montserrat",sans-serif;font-weight:700;font-style:italic;color:var(--green)}
  /* outside panel 1 */
  .tips{position:absolute;left:34px;right:26px;top:40px}
  .tips__list{list-style:none;margin-top:22px}
  .tip{display:flex;gap:10px;margin-bottom:16px;font-family:"Montserrat",sans-serif;font-style:italic;font-weight:500;font-size:11.5px;line-height:1.45;text-transform:uppercase;color:var(--text)}
  .tip__num{font-weight:700;font-size:17px;color:var(--green);flex:none;width:44px}
  .tips__note{font-size:9.5px;font-style:italic;line-height:1.5;color:#555;margin-top:6px}
  /* outside panel 2 */
  .contact{position:absolute;top:48px;left:0;right:0;text-align:center}
  .contact__title{font-family:"Montserrat",sans-serif;font-weight:700;color:var(--green);font-size:20px}
  .contact__sub{font-family:"Montserrat",sans-serif;font-weight:600;font-size:10.5px;text-transform:uppercase;line-height:1.4;margin-top:4px;color:var(--text)}
  .contact__icons{display:flex;justify-content:center;align-items:center;gap:8px;margin:14px auto 10px;width:240px}
  .contact__rule{flex:1;height:2px;background:var(--green)}
  .contact__lines{font-size:13px;line-height:1.5;text-align:left;padding-left:66px;color:var(--ink)}
  .brand--back{position:absolute;left:58px;bottom:80px}
  /* cover */
  .brand--cover{position:absolute;right:40px;top:70px}
  .cover__title{position:absolute;left:40px;bottom:110px;font-size:44px;color:var(--ink);letter-spacing:1px}
  .cover__title b{font-family:"Montserrat",sans-serif;font-weight:700;color:var(--ink)}
  .cover__url{position:absolute;left:34px;right:22px;bottom:44px;height:50px;border-radius:25px;background:var(--green);color:#fff;display:flex;align-items:center;justify-content:center;font-size:15.5px;letter-spacing:.8px}
  /* inside */
  .order{position:absolute;left:30px;right:26px;top:40px}
  .order__intro{font-size:15px;line-height:1.35;color:var(--ink);margin-top:12px}
  .bundle__title{font-family:"Montserrat",sans-serif;font-weight:700;font-size:14px;color:var(--ink);text-transform:uppercase}
  .bundle__title span{color:var(--green)}
  .bundle__desc{font-size:12px;line-height:1.35;color:var(--text);margin-top:2px}
  .bundle__list{list-style:none;margin-top:8px}
  .bundle__list li{font-size:12.5px;line-height:1;color:var(--text);display:flex;align-items:center;gap:10px;margin-bottom:8px}
  .bundle__list li::before{content:"";width:8px;height:8px;border-radius:50%;background:var(--green);flex:none}
  .bundle--harbour{position:absolute;left:30px;right:24px;top:390px}
  .bundle--meadow{position:absolute;left:30px;right:24px;top:130px}
  .bundle--hearth{position:absolute;left:26px;right:22px;top:246px}
  .closing{position:absolute;left:26px;right:22px;bottom:40px;font-family:"Montserrat",sans-serif;font-style:italic;font-weight:500;color:var(--green-dark);font-size:11.5px;line-height:1.45}
  .closing b{font-weight:700}
</style>
</head>
<body>

<section class="spread spread--outside">
  <div class="panel panel--tips">
    <div class="tips">
      <h2 class="heading">CLEANSE <i>TIPS.</i></h2>
      <ol class="tips__list">
        <li class="tip"><span class="tip__num">001.</span><span>Start each day with a 250ml glass of warm lemon water to kick-start early morning hydration, alkalization and elimination.</span></li>
        <li class="tip"><span class="tip__num">002.</span><span>Consume your juices at regular intervals throughout the day and finish each juice.</span></li>
        <li class="tip"><span class="tip__num">003.</span><span>Shake before consuming and chew your juice like food to get the digestive enzymes working for you.</span></li>
        <li class="tip"><span class="tip__num">004.</span><span>Exercise does wonders for distracting from hunger and clearing the head… just keep moving!</span></li>
        <li class="tip"><span class="tip__num">005.</span><span>Cleansing affects people differently with a variety of side effects that might arise including headaches, nausea, fatigue and irritability. Breathe deeply and repeat… this too shall pass!</span></li>
      </ol>
      <p class="tips__note">No added sugar / No concentrates / No preservatives / Dairy free Australian made &amp; owned / Cold Pressed from 100% whole fruits &amp; vegetables</p>
    </div>
    <div class="photo photo--bottles" role="img" aria-label="Row of cold pressed juice bottles in green, orange, red and cream with scattered fruit and flowers" style="left:0;right:0;bottom:0;height:150px;border-radius:0"></div>
  </div>

  <div class="panel panel--contact">
    <div class="contact">
      <h3 class="contact__title">CONTACT US</h3>
      <p class="contact__sub">About cold pressed juice<br>and juice cleanses!</p>
      <div class="contact__icons">
        <span class="contact__rule"></span>
        <svg width="14" height="14" viewBox="0 0 24 24" aria-hidden="true"><path fill="#3cb33e" d="M6.6 10.8a15.5 15.5 0 0 0 6.6 6.6l2.2-2.2a1 1 0 0 1 1-.25 11.4 11.4 0 0 0 3.6.57 1 1 0 0 1 1 1V20a1 1 0 0 1-1 1A17 17 0 0 1 3 4a1 1 0 0 1 1-1h3.5a1 1 0 0 1 1 1c0 1.25.2 2.45.57 3.57a1 1 0 0 1-.25 1z"/></svg>
        <svg width="16" height="12" viewBox="0 0 24 18" aria-hidden="true"><rect x="1" y="1" width="22" height="16" rx="2" fill="none" stroke="#3cb33e" stroke-width="2"/><path d="M1 2l11 8 11-8" fill="none" stroke="#3cb33e" stroke-width="2"/></svg>
        <span class="contact__rule"></span>
      </div>
      <p class="contact__lines">juice@brightmarlowtonic.com.au<br>0400555018<br>www.brightmarlowtonic.com.au</p>
    </div>
    <div class="brand brand--back"><span class="brand__dot"></span>brightmarlow</div>
  </div>

  <div class="panel panel--cover">
    <div class="brand brand--cover"><span class="brand__dot"></span>brightmarlow</div>
    <h1 class="heading cover__title">CLEANSE <b>TIPS</b></h1>
    <div class="cover__url">www.brightmarlowtonic.com.au</div>
  </div>

  <div class="photo photo--table" role="img" aria-label="Flat lay of green and cream juice bottles among mint leaves, apple halves, limes and herbs on white" style="left:390px;top:250px;width:710px;height:380px"></div>
</section>

<section class="spread spread--inside">
  <div class="panel panel--harbour">
    <div class="order">
      <h2 class="heading">CLEANSE <b>ORDER.</b></h2>
      <p class="order__intro">Upon waking, drink your first juice, and drink your next juice in order every two hours thereafter.</p>
    </div>
    <div class="photo photo--bottles" role="img" aria-label="Six juice bottles in a row: greens, orange, red, green and cream" style="left:30px;right:30px;top:190px;height:170px"></div>
    <div class="bundle bundle--harbour">
      <h3 class="bundle__title"><span>Harbour</span> Cleanse</h3>
      <p class="bundle__desc">This is our most popular cleanse &amp; perfect for those who want to balance great-tasting juices with high efficiency. This bundle includes:</p>
      <ul class="bundle__list">
        <li>Greens Smoothie</li><li>Ember Fizzwater or Spicy red</li><li>Green A</li><li>Red or Sweet Carrot</li><li>Green B</li><li>Either Silk Pour</li>
      </ul>
    </div>
    <div class="photo photo--greens" role="img" aria-label="Tops of cream and green juice bottles" style="left:0;right:0;bottom:0;height:120px;border-radius:0;background:linear-gradient(90deg,#e6d3c0,#efe6d6 40%,#5fae3c 60%,#4aa336)"></div>
  </div>

  <div class="panel panel--meadow">
    <div class="photo photo--bottles" role="img" aria-label="Upside-down juice bottle bases in orange, red and yellow" style="left:0;right:0;top:0;height:100px;border-radius:0;background:linear-gradient(90deg,#e8652a,#8c1f3a 35%,#f0b52a 65%,#e8782a)"></div>
    <div class="bundle bundle--meadow">
      <h3 class="bundle__title"><span>Meadow</span> Cleanse</h3>
      <p class="bundle__desc">Our most intense &amp; lowest calorie cleanse - you get the maximum results in the minimum amount of time. This bundle includes:</p>
      <ul class="bundle__list">
        <li>Fern Kick or Celery</li><li>Ember Fizzwater</li><li>Green Smoothie</li><li>Green B</li><li>Green A</li><li>Oatbloom Drinkable</li>
      </ul>
    </div>
    <div class="photo photo--greens" role="img" aria-label="Six green, yellow and cream juice bottles in a row" style="left:30px;right:30px;top:400px;height:180px"></div>
    <div class="photo photo--greens" role="img" aria-label="Tops of green juice bottles" style="left:0;right:0;bottom:0;height:130px;border-radius:0;background:linear-gradient(90deg,#4aa336,#6cc04a 50%,#4aa336)"></div>
  </div>

  <div class="panel panel--hearth">
    <div class="photo photo--bottles" role="img" aria-label="Bottle bases at top and a group of green, red, orange juices with a jar of bone broth" style="left:20px;right:20px;top:0;height:220px;border-radius:0 0 4px 4px;background:linear-gradient(180deg,#f3f3f3 0%,#f0a12a 18%,#f7f7f7 32%,#5fae3c 55%,#8c1f3a 70%,#e2612a 82%,#e6d3c0 100%)"></div>
    <div class="bundle bundle--hearth">
      <h3 class="bundle__title"><span>Hearth</span> Cleanse</h3>
      <p class="bundle__desc">The organic Hearth Cleanse. We've curated a mixture of smoothies, cold-pressed juices, bone broth and nut mylks to keep you clean and warm through the winter months. The broth together with our Ember Fizzwater and Oatbloom Drinkable can all be gently heated on the stove to nourish you from the inside and out. This bundle includes:</p>
      <ul class="bundle__list">
        <li>Green Smoothie</li><li>Ember Fizzwater or Spicy Red</li><li>Sweet Carrot or Red</li><li>Organic Bone Broth</li><li>Green B</li><li>Either Silk Pour</li>
      </ul>
    </div>
    <p class="closing">We truly believe in our Cleanses and the results speak for themselves. <b>NOURISH</b> your body with antioxidant-rich juices. <b>HELP</b> your digestion and encourage a healthy balance of flora in your belly. <b>ENJOY</b> better overall well-being and weight loss.</p>
  </div>
</section>

</body>
</html>
```